Redesign of our homepage

We are a company that operates in the Wellness tourism sector. We are starting a project to redesign our homepage. See the screenshots. The main idea is that the banner image and the text on the banner are dynamically replaced depending on whether a user clicks on the "Thumb up" or the "Thumb down" icon.
You can see a live version of our homepage at http://demo.velqorambe.com

Requirements
Must have
• Must abide by style and look & feel of the current site.
It is important to demonstrate the functionality that enables the banner image and text being refreshed at each click of a ThumbUp or ThumbDown icons. In others words the Javascript must work.

Let me add some more context on the project.

Actually the thumb up and thumb down are possible answers to question/comment dynamically displayed at the location of the current text "Experience That Make You tell an unforgettable story".
An example of a comment/question is "I need a program that would help limit my stress levels and make me look great and feel fantastic". Or "I need an activity that will reduce my stress."
So a user would have to click on a thumb up or thumb down to approve or disapprove these questions/comments..
Based on this information, I think you could move the thumbs up to the left and right side of the text (the comment/question) respectively. And move the reset underneath in the middle.

Maybe it's a good idea to reduce the font size of that text as well.

And now to the dropdown list. We need only 2 of them, and not 3 as you have displayed.
One of them contain the list:
-- I need a weekend retreat
-- ! need a week or more retreat
The other would contain a list of countries.
The drop down values must be selected before the thumbs up and down thumbs are active.
Therefore you should move them above the question/comment text.
And finally about the thumbs and reset icons. Please put them in a round orange color and make them a bit bigger.

```html
<!DOCTYPE html>
<html lang="en">
<head>
<meta charset="utf-8">
<title>Velqorambe – Wellness Retreats</title>
<link href="https://fonts.googleapis.com/css2?family=Lato:wght@400;700;900&display=swap" rel="stylesheet">
<style>
:root{
  --orange:#f5921e;
  --orange-dark:#e07f0c;
  --mint:#86d9c1;
  --mint-deep:#5fc6a6;
  --peach:#fde4cf;
  --ink:#1d1d1d;
  --text:#4a4a4a;
  --muted:#8a8a8a;
  --line:#e6e6e6;
  --green:#2e9b2e;
  --red:#e0312b;
  --black:#000;
  --white:#fff;
}
*{box-sizing:border-box;margin:0;padding:0}
html,body{width:1200px;height:3593px;overflow:hidden}
body{position:relative;font-family:'Lato',Arial,sans-serif;color:var(--text);background:var(--white);font-size:15px}
.abs{position:absolute}
svg{display:block}
sub{font-size:9px;line-height:0;vertical-align:-2px}

/* header */
.site-header{top:0;left:0;width:1200px;height:88px;display:flex;align-items:center;padding:0 112px;background:var(--white)}
.brand{font-size:34px;color:var(--orange);font-weight:400;letter-spacing:.5px;width:260px}
.main-nav{display:flex;align-items:center;gap:28px;font-size:14px;font-weight:700;color:var(--ink)}
.main-nav a{display:flex;align-items:center;gap:6px;color:inherit;text-decoration:none}
.main-nav .active{color:var(--orange)}
.auth{margin-left:auto;display:flex;gap:10px}
.btn{background:var(--orange);color:var(--white);font-weight:700;font-size:13px;border:0;border-radius:3px;display:inline-flex;align-items:center;gap:6px;padding:0 14px;height:36px}

/* hero */
.hero{top:88px;left:0;width:1200px;height:482px;text-align:center;color:var(--white)}
.hero-photo{position:absolute;inset:0;background:linear-gradient(180deg,#2a5fa6 0%,#5a8fcc 28%,#8fbfd8 48%,#3d9aa4 62%,#3f5a52 78%,#6e5a3e 100%)}
.selectors{position:relative;padding-top:64px;display:flex;justify-content:center;gap:17px}
.selectors .field{width:300px;height:40px;background:var(--white);border-radius:2px;display:flex;align-items:center;gap:8px;padding:0 12px;color:var(--muted);font-size:14px;text-align:left}
.selectors .field .arrow{margin-left:auto;font-size:9px;color:#444}
.question{position:relative;margin-top:40px;display:flex;justify-content:center;align-items:center;gap:32px}
.question h1{width:620px;font-size:26px;font-weight:900;line-height:34px;text-transform:uppercase;letter-spacing:.5px;text-shadow:0 1px 3px rgba(0,0,0,.35)}
.hero .tagline{position:relative;margin-top:12px;font-size:18px}
.round{width:58px;height:58px;border-radius:50%;background:var(--orange);display:flex;align-items:center;justify-content:center;flex:none;box-shadow:0 2px 6px rgba(0,0,0,.25)}
.reset-row{position:relative;margin-top:20px;display:flex;justify-content:center}

/* filters */
.filters{top:527px;left:112px;width:976px;height:223px;background:var(--white);box-shadow:0 4px 14px rgba(0,0,0,.14);display:flex}
.filter{flex:1;border-right:1px solid var(--line)}
.filter:last-child{border-right:0}
.filter h3{height:40px;line-height:40px;padding-left:18px;background:var(--mint);color:var(--white);font-size:15px;font-weight:700;text-transform:uppercase;border-right:1px solid var(--white)}
.filter ul{list-style:none;padding:8px 18px}
.filter li{font-size:13px;color:var(--text);height:39px;display:flex;align-items:center;justify-content:space-between;border-bottom:1px solid var(--line)}
.filter.compact li{height:29px;border:0;justify-content:flex-start;gap:8px}
.caret{color:var(--orange);font-size:11px}

/* offers */
.peach{background:var(--peach);width:86px;height:132px}
.offer{left:112px;width:976px}
.offer-text{position:absolute;width:400px}
.offer-text h2{font-size:27px;font-weight:700;color:var(--ink);line-height:36px}
.from{margin-top:16px;font-size:12px;color:var(--ink)}
.price{font-size:19px;color:var(--orange);margin-top:2px}
.price-for{font-size:12px;color:var(--ink);margin-top:6px}
.specs{list-style:none;margin-top:8px}
.specs li{display:flex;align-items:center;gap:12px;font-size:14px;color:var(--text);height:26px}
.impact{display:flex;gap:50px;margin-top:16px;font-size:14px;color:var(--ink)}
.impact span{display:flex;align-items:center;gap:8px}
.offer .btn{margin-top:24px;height:40px;padding:0 20px}
.offer-media{position:absolute;width:559px;box-shadow:0 4px 14px rgba(0,0,0,.15);background:var(--white)}
.photo{height:316px}
.perks{display:flex;height:107px}
.perk{flex:1;display:flex;flex-direction:column;justify-content:center;padding:0 0 0 38px;border-right:1px solid var(--line);position:relative}
.perk:last-child{border:0}
.perk .row{display:flex;align-items:center;gap:14px;font-size:13px;color:var(--muted);line-height:16px}
.perk .mark{margin:10px 0 0 58px}
.divider{left:112px;width:976px;height:1px;background:var(--line)}

/* pagination */
.pager{top:2455px;left:0;width:1200px;display:flex;justify-content:center;gap:6px}
.pager a{min-width:32px;height:32px;padding:0 10px;display:flex;align-items:center;justify-content:center;font-size:13px;font-weight:700;color:var(--ink);border:1px solid var(--line);text-decoration:none;background:var(--white)}
.pager a.current{background:var(--orange);border-color:var(--orange);color:var(--white)}
.pager a.wide{padding:0 14px}

/* stats */
.stats{top:2558px;left:0;width:1200px;height:503px;display:flex}
.stats .half{flex:1;position:relative}
.stats .mint{background:var(--mint)}
.stats .orange{background:var(--orange)}
.chart-card{position:absolute;top:82px;width:386px;height:337px;background:var(--white);border:8px solid rgba(255,255,255,.55);background-clip:padding-box;text-align:center;box-shadow:0 2px 8px rgba(0,0,0,.12)}
.chart-card h4{font-size:19px;font-weight:400;color:var(--ink);margin-top:14px}
.chart-card p{font-size:11px;color:var(--muted);margin-top:6px}
.chart-card svg{margin:6px auto 0}
.legend{display:flex;flex-wrap:wrap;gap:4px 30px;padding:4px 18px;font-size:9px;color:var(--text);text-align:left}
.legend i{display:inline-block;width:8px;height:8px;border-radius:50%;margin-right:4px;vertical-align:-1px}

/* newsletter */
.newsletter{top:3061px;left:0;width:1200px;height:134px;background:var(--black);color:var(--white);padding:34px 112px 0}
.newsletter h2{font-size:27px;font-weight:400;letter-spacing:.5px}
.newsletter p{font-size:13px;color:#bdbdbd;margin-top:8px}
.subscribe{position:absolute;top:46px;left:678px;display:flex}
.subscribe .input{width:304px;height:38px;background:var(--white);display:flex;align-items:center;gap:10px;padding:0 12px;font-size:13px;color:var(--muted)}
.subscribe .btn{height:38px;border-radius:0;width:106px;justify-content:center;font-size:14px}

/* footer */
.site-footer{top:3195px;left:0;width:1200px;height:350px}
.col{position:absolute;top:66px}
.col h5{font-size:15px;font-weight:700;color:var(--ink);text-transform:uppercase;margin-bottom:16px}
.col ul{list-style:none}
.col li{font-size:13px;line-height:23px;color:var(--text)}
.contact-row{display:flex;align-items:center;gap:16px;font-size:15px;color:var(--ink);margin-bottom:20px}
.ico-box{width:32px;height:32px;border-radius:3px;display:flex;align-items:center;justify-content:center}
.ico-box.solid{background:var(--orange)}
.ico-box.outline{border:1px solid var(--line)}
.social{display:flex;gap:16px}
.social span{width:30px;height:30px;border:1px solid var(--line);border-radius:3px;display:flex;align-items:center;justify-content:center}
.social span i{width:12px;height:12px;border-radius:50%;background:var(--orange);display:block}
.legal{width:150px;font-size:13px;line-height:20px;color:var(--text)}
.bottom-bar{top:3545px;left:112px;width:976px;height:48px;border-top:1px solid var(--line);display:flex;align-items:center;font-size:12px;color:var(--muted)}
</style>
</head>
<body>

<header class="site-header abs">
  <div class="brand">velqorambe</div>
  <nav class="main-nav">
    <a href="#">EUR <span style="font-size:9px">&#9660;</span></a>
    <a href="#" class="active">
      <svg width="16" height="14" viewBox="0 0 16 14"><path d="M8 13C3 10 1 7 2 4c1-3 4-3 6-1 2-2 5-2 6 1 1 3-1 6-6 9z" fill="var(--orange)"/></svg>
      Wellness Retreats</a>
    <a href="#">
      <svg width="18" height="12" viewBox="0 0 18 12"><path d="M4 12a4 4 0 0 1-.5-7.9A5 5 0 0 1 13 3a4.5 4.5 0 0 1 1 9z" fill="var(--ink)"/></svg>
      Our Climate Pledge</a>
    <a href="#">
      <svg width="18" height="12" viewBox="0 0 18 12"><rect x="1" y="3" width="16" height="7" rx="3.5" fill="none" stroke="var(--ink)" stroke-width="2"/></svg>
      Partners</a>
  </nav>
  <div class="auth">
    <span class="btn">
      <svg width="12" height="12" viewBox="0 0 12 12"><path d="M1 6h7M5 3l3 3-3 3M9 1h2v10H9" stroke="#fff" stroke-width="1.6" fill="none"/></svg>Sign in</span>
    <span class="btn">
      <svg width="13" height="12" viewBox="0 0 13 12"><circle cx="5" cy="3.5" r="2.8" fill="#fff"/><path d="M0 12c0-3 2-5 5-5s5 2 5 5z" fill="#fff"/><path d="M10 2v4M8 4h4" stroke="#fff" stroke-width="1.4"/></svg>Sign Up</span>
  </div>
</header>

<section class="hero abs">
  <div class="hero-photo" role="img" aria-label="Overwater bungalows on a turquoise lagoon under a blue sky with palm trees"></div>
  <div class="selectors">
    <div class="field"><svg width="13" height="13" viewBox="0 0 13 13"><rect x="1" y="2" width="11" height="10" fill="none" stroke="#666" stroke-width="1.5"/><path d="M1 5h11" stroke="#666" stroke-width="1.5"/></svg>I need a weekend retreat<span class="arrow">&#9660;</span></div>
    <div class="field"><svg width="10" height="14" viewBox="0 0 10 14"><path d="M5 14S0 8 0 5a5 5 0 0 1 10 0c0 3-5 9-5 9z" fill="#666"/><circle cx="5" cy="5" r="2" fill="#fff"/></svg>Choose a country<span class="arrow">&#9660;</span></div>
  </div>
  <div class="question">
    <span class="round" aria-label="Thumb up"><svg width="24" height="24" viewBox="0 0 18 18"><rect x="1" y="8" width="4" height="9" fill="#fff"/><path d="M6 8l4-7c2 0 2 2 1.5 4H16c1 0 2 1 1.5 2l-2 8c-.3 1-1 2-2 2H6z" fill="#fff"/></svg></span>
    <h1>Experiences that make you tell an<br>unforgettable story</h1>
    <span class="round" aria-label="Thumb down"><svg width="24" height="24" viewBox="0 0 18 18"><rect x="1" y="1" width="4" height="9" fill="#fff"/><path d="M6 10l4 7c2 0 2-2 1.5-4H16c1 0 2-1 1.5-2l-2-8c-.3-1-1-2-2-2H6z" fill="#fff"/></svg></span>
  </div>
  <p class="tagline">Incorporated With Climate Awareness</p>
  <div class="reset-row">
    <span class="round" aria-label="Reset"><svg width="24" height="24" viewBox="0 0 18 18"><path d="M4 5a6.5 6.5 0 1 1-1.5 5" fill="none" stroke="#fff" stroke-width="2"/><path d="M1 2v5h5z" fill="#fff"/></svg></span>
  </div>
</section>

<section class="filters abs">
  <div class="filter">
    <h3>Destinations</h3>
    <ul>
      <li>Europe <span class="caret">&#9776;</span></li>
      <li>Asia &amp; Oceania <span class="caret">&#9776;</span></li>
      <li>Africa &amp; Middle East <span class="caret">&#9776;</span></li>
      <li style="border:0">The Americas &amp; Caribbean <span class="caret">&#9776;</span></li>
    </ul>
  </div>
  <div class="filter">
    <h3>Categories</h3>
    <ul>
      <li>Health &amp; Wellness <span class="caret">&#9776;</span></li>
      <li>Culinary <span class="caret">&#9776;</span></li>
      <li>Safaris <span class="caret">&#9776;</span></li>
      <li style="border:0">Ranch <span class="caret">&#9776;</span></li>
    </ul>
  </div>
  <div class="filter compact">
    <h3>Duration</h3>
    <ul>
      <li><span class="caret">&#9654;</span>2 days</li>
      <li><span class="caret">&#9654;</span>From 3 to 7 days</li>
      <li><span class="caret">&#9654;</span>From 1 to 2 weeks</li>
      <li><span class="caret">&#9654;</span>From 2 to 3 weeks</li>
      <li><span class="caret">&#9654;</span>More than 3 weeks</li>
    </ul>
  </div>
  <div class="filter compact">
    <h3>Budget</h3>
    <ul>
      <li><span class="caret">&#9654;</span>Up to €120</li>
      <li><span class="caret">&#9654;</span>From €120 to €350</li>
      <li><span class="caret">&#9654;</span>From €350 to €1,500</li>
      <li><span class="caret">&#9654;</span>From €1,500 to €2,000</li>
      <li><span class="caret">&#9654;</span>More than €2,000</li>
    </ul>
  </div>
</section>

<div class="abs peach" style="top:970px;left:1114px"></div>
<div class="abs peach" style="top:1533px;left:0"></div>
<div class="abs peach" style="top:2108px;left:1114px"></div>

<article class="offer abs" style="top:815px">
  <div class="offer-text" style="left:0;top:0">
    <h2>3 Days Big Five Tented Safari, Kruger National Park, South Africa</h2>
    <p class="from">from</p>
    <p class="price">€370.00</p>
    <p class="price-for">Price for:</p>
    <ul class="specs">
      <li><svg width="13" height="13" viewBox="0 0 13 13"><rect x="1" y="2" width="11" height="10" fill="#333"/></svg>3 days / 2 nights</li>
      <li><svg width="13" height="13" viewBox="0 0 13 13"><circle cx="6.5" cy="4" r="3" fill="#333"/><path d="M1 13c0-3 2.5-5 5.5-5s5.5 2 5.5 5z" fill="#333"/></svg>Minimum number of persons: 1</li>
      <li><svg width="13" height="13" viewBox="0 0 13 13"><circle cx="6.5" cy="4" r="3" fill="#333"/><path d="M1 13c0-3 2.5-5 5.5-5s5.5 2 5.5 5z" fill="#333"/></svg>Maximum group size: 8</li>
      <li><svg width="13" height="13" viewBox="0 0 13 13"><circle cx="6.5" cy="4" r="3" fill="#333"/><path d="M1 13c0-3 2.5-5 5.5-5s5.5 2 5.5 5z" fill="#333"/></svg>Minimum age: 10 years</li>
    </ul>
    <div class="impact">
      <span><svg width="26" height="20" viewBox="0 0 26 20"><path d="M6 18a5 5 0 0 1-1-9.9A7 7 0 0 1 18 6a6 6 0 0 1 2 12z" fill="var(--mint-deep)"/></svg>3.02 tCO<sub>2</sub>(e)</span>
      <span><svg width="22" height="22" viewBox="0 0 22 22"><circle cx="11" cy="9" r="8" fill="var(--mint-deep)"/><rect x="10" y="14" width="2" height="8" fill="#8a6a3a"/></svg>193 trees</span>
    </div>
    <span class="btn">SEE DETAILS &#8594;</span>
  </div>
  <div class="offer-media" style="left:417px;top:7px">
    <div class="photo" role="img" aria-label="Safari guide in red robes standing beside a giraffe on the savanna" style="background:linear-gradient(180deg,#a9b7bf 0%,#9aa173 45%,#7a7a3e 70%,#5d5a2c 100%)"></div>
    <div class="perks">
      <div class="perk"><div class="row"><svg width="24" height="18" viewBox="0 0 24 18"><rect x="1" y="2" width="22" height="14" rx="2" fill="var(--mint-deep)"/><rect x="1" y="6" width="22" height="3" fill="#fff"/></svg>Flexible<br>Cancellation<br>Policy</div><svg class="mark" width="16" height="14" viewBox="0 0 16 14"><path d="M1 7l5 5L15 1" stroke="var(--green)" stroke-width="3" fill="none"/></svg></div>
      <div class="perk"><div class="row"><svg width="24" height="22" viewBox="0 0 24 22"><path d="M12 1l2 7 9 4v2l-9-2-1 6 3 2v1l-4-1-4 1v-1l3-2-1-6-9 2v-2l9-4z" fill="var(--mint-deep)"/></svg>Airport<br>Transfer<br>Included</div><svg class="mark" width="14" height="14" viewBox="0 0 14 14"><path d="M2 2l10 10M12 2L2 12" stroke="var(--red)" stroke-width="3"/></svg></div>
      <div class="perk"><div class="row"><svg width="24" height="22" viewBox="0 0 24 22"><circle cx="12" cy="11" r="9" fill="none" stroke="var(--mint-deep)" stroke-width="2"/><circle cx="12" cy="11" r="4" fill="var(--mint-deep)"/></svg>Meals<br>Included</div><svg class="mark" width="16" height="14" viewBox="0 0 16 14"><path d="M1 7l5 5L15 1" stroke="var(--green)" stroke-width="3" fill="none"/></svg></div>
    </div>
  </div>
</article>

<div class="divider abs" style="top:1317px"></div>

<article class="offer abs" style="top:1390px">
  <div class="offer-media" style="left:0;top:0">
    <div class="photo" role="img" aria-label="Rider on horseback roping a calf in a fenced ranch corral with hills behind" style="background:linear-gradient(180deg,#b9d4ea 0%,#c8c4b0 30%,#a39a6e 50%,#c9b48a 75%,#d8c7a4 100%)"></div>
    <div class="perks">
      <div class="perk"><div class="row"><svg width="24" height="18" viewBox="0 0 24 18"><rect x="1" y="2" width="22" height="14" rx="2" fill="var(--mint-deep)"/><rect x="1" y="6" width="22" height="3" fill="#fff"/></svg>Flexible<br>Cancellation<br>Policy</div><svg class="mark" width="16" height="14" viewBox="0 0 16 14"><path d="M1 7l5 5L15 1" stroke="var(--green)" stroke-width="3" fill="none"/></svg></div>
      <div class="perk"><div class="row"><svg width="24" height="22" viewBox="0 0 24 22"><path d="M12 1l2 7 9 4v2l-9-2-1 6 3 2v1l-4-1-4 1v-1l3-2-1-6-9 2v-2l9-4z" fill="var(--mint-deep)"/></svg>Airport<br>Transfer<br>Included</div><svg class="mark" width="14" height="14" viewBox="0 0 14 14"><path d="M2 2l10 10M12 2L2 12" stroke="var(--red)" stroke-width="3"/></svg></div>
      <div class="perk"><div class="row"><svg width="24" height="22" viewBox="0 0 24 22"><circle cx="12" cy="11" r="9" fill="none" stroke="var(--mint-deep)" stroke-width="2"/><circle cx="12" cy="11" r="4" fill="var(--mint-deep)"/></svg>Meals<br>Included</div><svg class="mark" width="16" height="14" viewBox="0 0 16 14"><path d="M1 7l5 5L15 1" stroke="var(--green)" stroke-width="3" fill="none"/></svg></div>
    </div>
  </div>
  <div class="offer-text" style="left:623px;top:0;width:370px">
    <h2>2 Days Wild West Ranch Explo-<br>ration And Bike Holiday In Colorado, USA</h2>
    <p class="from">from</p>
    <p class="price">€384.00</p>
    <p class="price-for">Price for:</p>
    <ul class="specs">
      <li><svg width="13" height="13" viewBox="0 0 13 13"><rect x="1" y="2" width="11" height="10" fill="#333"/></svg>2 days / 1 nights</li>
      <li><svg width="13" height="13" viewBox="0 0 13 13"><circle cx="6.5" cy="4" r="3" fill="#333"/><path d="M1 13c0-3 2.5-5 5.5-5s5.5 2 5.5 5z" fill="#333"/></svg>Minimum number of persons: 1</li>
      <li><svg width="13" height="13" viewBox="0 0 13 13"><circle cx="6.5" cy="4" r="3" fill="#333"/><path d="M1 13c0-3 2.5-5 5.5-5s5.5 2 5.5 5z" fill="#333"/></svg>Maximum group size: 5</li>
      <li><svg width="13" height="13" viewBox="0 0 13 13"><circle cx="6.5" cy="4" r="3" fill="#333"/><path d="M1 13c0-3 2.5-5 5.5-5s5.5 2 5.5 5z" fill="#333"/></svg>Minimum age: 13 years</li>
    </ul>
    <div class="impact">
      <span><svg width="26" height="20" viewBox="0 0 26 20"><path d="M6 18a5 5 0 0 1-1-9.9A7 7 0 0 1 18 6a6 6 0 0 1 2 12z" fill="var(--mint-deep)"/></svg>2.51 tCO<sub>2</sub>(e)</span>
      <span><svg width="22" height="22" viewBox="0 0 22 22"><circle cx="11" cy="9" r="8" fill="var(--mint-deep)"/><rect x="10" y="14" width="2" height="8" fill="#8a6a3a"/></svg>160 trees</span>
    </div>
    <span class="btn">SEE DETAILS &#8594;</span>
  </div>
</article>

<div class="divider abs" style="top:1892px"></div>

<article class="offer abs" style="top:1955px">
  <div class="offer-text" style="left:0;top:0">
    <h2>5 Days Full Ranch Experience And Horsemanship Training In Mulla Creek, NSW, Australia</h2>
    <p class="from">from</p>
    <p class="price">€458.00</p>
    <p class="price-for">Price for:</p>
    <ul class="specs">
      <li><svg width="13" height="13" viewBox="0 0 13 13"><rect x="1" y="2" width="11" height="10" fill="#333"/></svg>5 days / 4 nights</li>
      <li><svg width="13" height="13" viewBox="0 0 13 13"><circle cx="6.5" cy="4" r="3" fill="#333"/><path d="M1 13c0-3 2.5-5 5.5-5s5.5 2 5.5 5z" fill="#333"/></svg>Minimum number of persons: 1</li>
      <li><svg width="13" height="13" viewBox="0 0 13 13"><circle cx="6.5" cy="4" r="3" fill="#333"/><path d="M1 13c0-3 2.5-5 5.5-5s5.5 2 5.5 5z" fill="#333"/></svg>Maximum group size: 15</li>
      <li><svg width="13" height="13" viewBox="0 0 13 13"><circle cx="6.5" cy="4" r="3" fill="#333"/><path d="M1 13c0-3 2.5-5 5.5-5s5.5 2 5.5 5z" fill="#333"/></svg>Minimum age: 15 years</li>
    </ul>
    <div class="impact">
      <span><svg width="26" height="20" viewBox="0 0 26 20"><path d="M6 18a5 5 0 0 1-1-9.9A7 7 0 0 1 18 6a6 6 0 0 1 2 12z" fill="var(--mint-deep)"/></svg>5.26 tCO<sub>2</sub>(e)</span>
      <span><svg width="22" height="22" viewBox="0 0 22 22"><circle cx="11" cy="9" r="8" fill="var(--mint-deep)"/><rect x="10" y="14" width="2" height="8" fill="#8a6a3a"/></svg>335 trees</span>
    </div>
    <span class="btn">SEE DETAILS &#8594;</span>
  </div>
  <div class="offer-media" style="left:417px;top:5px">
    <div class="photo" role="img" aria-label="Group of riders on horseback following a fenced track through green fields" style="background:linear-gradient(180deg,#b6cfe6 0%,#8fae7a 35%,#5f8a3e 60%,#8b8a6a 85%,#a59a7c 100%)"></div>
    <div class="perks">
      <div class="perk"><div class="row"><svg width="24" height="18" viewBox="0 0 24 18"><rect x="1" y="2" width="22" height="14" rx="2" fill="var(--mint-deep)"/><rect x="1" y="6" width="22" height="3" fill="#fff"/></svg>Flexible<br>Cancellation<br>Policy</div><svg class="mark" width="16" height="14" viewBox="0 0 16 14"><path d="M1 7l5 5L15 1" stroke="var(--green)" stroke-width="3" fill="none"/></svg></div>
      <div class="perk"><div class="row"><svg width="24" height="22" viewBox="0 0 24 22"><path d="M12 1l2 7 9 4v2l-9-2-1 6 3 2v1l-4-1-4 1v-1l3-2-1-6-9 2v-2l9-4z" fill="var(--mint-deep)"/></svg>Airport<br>Transfer<br>Included</div><svg class="mark" width="14" height="14" viewBox="0 0 14 14"><path d="M2 2l10 10M12 2L2 12" stroke="var(--red)" stroke-width="3"/></svg></div>
      <div class="perk"><div class="row"><svg width="24" height="22" viewBox="0 0 24 22"><circle cx="12" cy="11" r="9" fill="none" stroke="var(--mint-deep)" stroke-width="2"/><circle cx="12" cy="11" r="4" fill="var(--mint-deep)"/></svg>Meals<br>Included</div><svg class="mark" width="16" height="14" viewBox="0 0 16 14"><path d="M1 7l5 5L15 1" stroke="var(--green)" stroke-width="3" fill="none"/></svg></div>
    </div>
  </div>
</article>

<div class="divider abs" style="top:2471px"></div>
<nav class="pager abs">
  <a href="#" class="wide">PREV</a>
  <a href="#" class="current">1</a>
  <a href="#">2</a>
  <a href="#">3</a>
  <a href="#">4</a>
  <a href="#" class="wide">NEXT</a>
</nav>

<section class="stats abs">
  <div class="half mint">
    <div class="chart-card" style="left:112px">
      <h4>Carbon footprint</h4>
      <p>Total carbon footprint from booked vacations on our site</p>
      <svg width="340" height="200" viewBox="0 0 340 200" aria-label="Pie chart of carbon footprint">
        <path d="M40 95v30a120 55 0 0 0 240 0V95z" fill="#4fb89a"/>
        <ellipse cx="160" cy="95" rx="120" ry="55" fill="var(--mint)"/>
        <path d="M160 95L40 95A120 55 0 0 1 278 84z" fill="var(--orange)"/>
        <path d="M160 95L278 84A120 55 0 0 1 280 98z" fill="#1f5fb0"/>
        <text x="150" y="32" font-size="8" fill="#555" font-family="Lato,sans-serif">2,134 tCO2e</text>
        <text x="288" y="92" font-size="8" fill="#555" font-family="Lato,sans-serif">128 tCO2e</text>
        <text x="40" y="175" font-size="8" fill="#555" font-family="Lato,sans-serif">2,004 tCO2e</text>
      </svg>
      <div class="legend">
        <span><i style="background:#1f5fb0"></i>Not yet offset, 2.99%</span>
        <span><i style="background:var(--orange)"></i>Offset by Velqorambe, 40%</span>
        <span><i style="background:var(--mint)"></i>Offset by customers, 57.01%</span>
      </div>
    </div>
  </div>
  <div class="half orange">
    <div class="chart-card" style="left:100px">
      <h4>Tress</h4>
      <p>Total trees to offset booked vacations on our site</p>
      <svg width="340" height="200" viewBox="0 0 340 200" aria-label="Pie chart of trees planted">
        <path d="M40 95v30a120 55 0 0 0 240 0V95z" fill="#4fb89a"/>
        <ellipse cx="160" cy="95" rx="120" ry="55" fill="var(--mint)"/>
        <path d="M160 95L40 95A120 55 0 0 1 278 84z" fill="var(--orange)"/>
        <path d="M160 95L278 84A120 55 0 0 1 280 98z" fill="#1f5fb0"/>
        <text x="150" y="32" font-size="8" fill="#555" font-family="Lato,sans-serif">370 trees</text>
        <text x="288" y="92" font-size="8" fill="#555" font-family="Lato,sans-serif">44 trees</text>
        <text x="40" y="175" font-size="8" fill="#555" font-family="Lato,sans-serif">455 trees</text>
      </svg>
      <div class="legend">
        <span><i style="background:#1f5fb0"></i>Not yet planted, 2.99%</span>
        <span><i style="background:var(--orange)"></i>Planted by Velqorambe, 40%</span>
        <span><i style="background:var(--mint)"></i>Planted by customers, 57.01%</span>
      </div>
    </div>
  </div>
</section>

<section class="newsletter abs">
  <h2>NEWSLETTER SIGNUP</h2>
  <p>Nemo enim ipsam voluptatem quia voluptas sit aspernatur aut odit aut</p>
  <div class="subscribe">
    <div class="input"><svg width="14" height="11" viewBox="0 0 14 11"><rect x="1" y="1" width="12" height="9" fill="none" stroke="var(--orange)" stroke-width="1.5"/><path d="M1 1l6 5 6-5" stroke="var(--orange)" stroke-width="1.5" fill="none"/></svg>Enter your email address</div>
    <span class="btn">SIGN UP</span>
  </div>
</section>

<footer class="site-footer abs">
  <div class="col" style="left:112px">
    <h5>Contact Us</h5>
    <div class="contact-row"><span class="ico-box solid"><svg width="14" height="14" viewBox="0 0 14 14"><path d="M3 1l2 3-1.5 1.5a8 8 0 0 0 5 5L10 9l3 2-1 2.5C6 14 0 8 .5 2z" fill="#fff"/></svg></span>+ 01 234 567 88</div>
    <div class="contact-row" style="font-size:14px"><span class="ico-box outline"><svg width="14" height="11" viewBox="0 0 14 11"><rect x="1" y="1" width="12" height="9" fill="none" stroke="var(--orange)" stroke-width="1.5"/><path d="M1 1l6 5 6-5" stroke="var(--orange)" stroke-width="1.5" fill="none"/></svg></span>info@velqorambe.com</div>
    <div class="social"><span><i></i></span><span><i></i></span><span><i></i></span><span><i></i></span></div>
  </div>
  <div class="col" style="left:445px">
    <h5>Velqorambe</h5>
    <ul><li>About Us</li><li>Contact Us</li><li>Terms and Conditions</li><li>Privacy</li></ul>
  </div>
  <div class="col" style="left:613px">
    <h5>Sustainability</h5>
    <ul><li>Our Climate Pledge</li><li>Our Progress</li><li>How It Works</li></ul>
  </div>
  <div class="col" style="left:778px">
    <h5>Our Partners</h5>
    <ul><li>Organizers</li><li>Rootwell.org</li></ul>
  </div>
  <div class="col" style="left:948px">
    <h5>Legal Information</h5>
    <p class="legal">VELQORAMBE B.V. is registered with the trade register of the Chamber of Commerce in Utrecht, the Netherlands, under registration number 74764780.<br>VAT registration number is NL800000000B01.</p>
  </div>
</footer>

<div class="bottom-bar abs">© 2020 VELQORAMBE. All rights reserved.</div>

</body>
</html>
```